Top tier Window Cleaning in Greater Cincinnati , needs a business card design.

We need a business card design for a Window Cleaning business in Cincinnati, OH. Our name is Bright Meadow Window Cleaning, we offer Window Cleaning, Pressure Washing,Gutter Cleaning, Commercial or residential. We want something with a QR code to scan for a google review. We want a name on the front, Owner is Darnell Ruiz. Our phone number is 513-555-0173. Company email is Brightmeadow4@mailnest.com. We want a business card that is simple and sleek, and grabs attention.

```html
<!DOCTYPE html>
<html lang="en">
<head>
<meta charset="utf-8">
<title>Bright Meadow Window Cleaning – Business Card</title>
<link rel="stylesheet" href="https://fonts.googleapis.com/css2?family=Courier+Prime&family=Lato:wght@400;700&display=swap">
<style>
  :root {
    --backdrop: #2b2b2b;
    --card: #ffffff;
    --brand-blue: #0596d6;
    --ink: #444444;
    --white: #ffffff;
  }
  * { box-sizing: border-box; margin: 0; padding: 0; }
  html, body { width: 1200px; height: 875px; overflow: hidden; }
  body {
    background: var(--backdrop);
    font-family: "Lato", sans-serif;
    position: relative;
  }
  .card {
    position: absolute;
    left: 280px;
    width: 640px;
    height: 366px;
    background: var(--card);
    border-radius: 22px;
    overflow: hidden;
  }
  .card--front { top: 40px; }
  .card--back { top: 468px; }

  /* Front */
  .front-tagline {
    position: absolute;
    top: 40px; right: 60px;
    font-family: "Courier Prime", monospace;
    font-size: 22px;
    color: var(--ink);
  }
  .brand {
    display: flex;
    align-items: center;
    gap: 14px;
    font-family: "Lato", sans-serif;
    font-weight: 700;
    color: var(--brand-blue);
  }
  .brand-dot {
    flex: none;
    border-radius: 50%;
    background: var(--brand-blue);
  }
  .front-brand {
    position: absolute;
    top: 130px; left: 0; right: 0;
    justify-content: center;
    font-size: 26px;
  }
  .front-brand .brand-dot { width: 46px; height: 46px; }
  .services {
    position: absolute;
    left: 40px; bottom: 40px;
    font-size: 17px;
    line-height: 1.5;
    color: var(--ink);
  }

  /* Back */
  .back-sweep { position: absolute; inset: 0; }
  .back-brand {
    position: absolute;
    top: 150px; left: 40px;
    width: 220px;
    font-size: 17px;
    line-height: 1.25;
  }
  .back-brand .brand-dot { width: 30px; height: 30px; }
  .contact {
    position: absolute;
    right: 34px; top: 150px;
    text-align: right;
    color: var(--white);
  }
  .contact-name {
    font-size: 34px;
    font-weight: 400;
    letter-spacing: 0.5px;
    text-transform: uppercase;
  }
  .contact-role { font-size: 17px; margin-bottom: 12px; }
  .contact-line {
    display: flex;
    justify-content: flex-end;
    align-items: center;
    gap: 8px;
    font-size: 16px;
    line-height: 1.6;
  }
  .contact-icon { width: 14px; height: 14px; fill: var(--white); }
</style>
</head>
<body>
  <section class="card card--front">
    <p class="front-tagline">Bright Meadow</p>
    <div class="brand front-brand">
      <span class="brand-dot"></span>
      <span>Bright Meadow Window Cleaning</span>
    </div>
    <p class="services">
      Window Cleaning | Pressure Washing<br>
      Gutter Cleaning | Commercial &amp; residential
    </p>
  </section>

  <section class="card card--back">
    <svg class="back-sweep" width="640" height="366" viewBox="0 0 640 366">
      <path d="M150 366 C 250 180, 430 80, 640 55 L640 366 Z" fill="var(--brand-blue)"/>
    </svg>
    <div class="brand back-brand">
      <span class="brand-dot"></span>
      <span>Bright Meadow Window Cleaning</span>
    </div>
    <div class="contact">
      <p class="contact-name">Darnell Ruiz</p>
      <p class="contact-role">Owner</p>
      <p class="contact-line">513-555-0173
        <svg class="contact-icon" viewBox="0 0 24 24"><path d="M6.6 10.8a15.1 15.1 0 0 0 6.6 6.6l2.2-2.2c.3-.3.7-.4 1-.2 1.1.4 2.3.6 3.6.6.6 0 1 .4 1 1V20c0 .6-.4 1-1 1A17 17 0 0 1 3 4c0-.6.4-1 1-1h3.5c.6 0 1 .4 1 1 0 1.3.2 2.5.6 3.6.1.3 0 .7-.2 1z"/></svg>
      </p>
      <p class="contact-line">Brightmeadow4@mailnest.com
        <svg class="contact-icon" viewBox="0 0 24 24"><path d="M2 5h20v14H2z M3.5 6.5 12 13l8.5-6.5" fill="var(--white)" stroke="var(--brand-blue)" stroke-width="1.5"/></svg>
      </p>
    </div>
  </section>
</body>
</html>
```